Business Card Design

Retail Do It Yourself Studio/Store
I sell Lena Marsh Clay Paint and supplies to repurpose furniture. Classes are held to teach basic chalk paint techniques. Lena Marsh Quick Coat Paint does not require sanding or primer. It is not only perfect for furniture but Kitchen and Bathroom cabinets. Other classes include painting with laquer,painting with milk paint, antiquing mirrors, using zinc on stainless steel. Painting on fabric, upholstery, repurposing garage sale finds. Taking your $5 dollar item and turning it into a one of kind interior design masterpiece. Studio time is also sold. Patrons may come for a one time visit and use our paint and supplies to repurpose their furniture or they may want a membership to come anytime they want to use our supplies to work on their pieces. I will also consign repurposed pieces in the store, at local antique markets and online.

Industry/Entity Type

Painting

Contact Information for Business Card

Dora Pell
218 Wexley Blvd. Suite 407
Marlow Bay, Florida 32990
321-555-0264
https://www.example-social.test/velvetoakworkshop

```html
<!DOCTYPE html>
<html lang="en">
<head>
<meta charset="utf-8">
<title>Velvet Oak Workshop – Business Card</title>
<link rel="stylesheet" href="https://fonts.googleapis.com/css2?family=Cinzel:wght@400;500&family=Tinos&display=swap">
<style>
  :root {
    --backdrop: #5e5048;
    --card-white: #ffffff;
    --ink: #1a1a1a;
    --teal: #1a9bb8;
    --violet: #3e2f8c;
    --charcoal: #17232a;
    --light-text: #ffffff;
  }
  * { margin: 0; padding: 0; box-sizing: border-box; }
  html, body {
    width: 1200px; height: 1200px; overflow: hidden;
    background: var(--backdrop);
  }
  .canvas { position: relative; width: 1200px; height: 1200px; }

  .card {
    position: absolute; left: 120px; width: 954px;
    background: var(--card-white);
    overflow: hidden;
  }
  .card--front { top: 24px; height: 558px; }
  .card--back  { top: 610px; height: 556px; background: var(--charcoal); }

  .brand {
    position: absolute; top: 0; left: 0; width: 100%; height: 336px;
    text-align: center; color: var(--ink);
  }
  .brand__name {
    font-family: "Cinzel", serif; font-weight: 400;
    font-size: 64px; line-height: 1.05; letter-spacing: 3px;
    padding-top: 62px;
  }
  .brand__tagline {
    font-family: "Tinos", serif;
    font-size: 35px; letter-spacing: 7px;
    margin-top: 46px;
  }

  .band { position: absolute; left: 0; width: 100%; color: var(--light-text); text-align: center; }
  .band--name {
    top: 336px; height: 48px; background: var(--teal);
    font-family: "Cinzel", serif; font-weight: 500; font-size: 34px; line-height: 48px; letter-spacing: 1px;
  }
  .band--address {
    top: 384px; height: 84px; background: var(--violet);
    font-family: "Tinos", serif; font-style: normal; font-size: 26px; line-height: 34px; padding-top: 8px;
  }
  .band--contact {
    top: 468px; height: 90px; background: var(--charcoal);
    font-family: "Tinos", serif; font-size: 25px; line-height: 32px; padding-top: 14px;
  }

  .photo { position: absolute; }
  .photo--dining  { left: 0;   top: 0;   width: 294px; height: 312px; z-index: 2; background: linear-gradient(160deg, #3aa6b0 0%, #d9d6cf 35%, #c9c6bc 70%, #c9c35a 100%); }
  .photo--stools  { left: 294px; top: 0; width: 306px; height: 248px; background: linear-gradient(150deg, #e9e7e2 0%, #2e8fc4 50%, #7a4b2f 100%); }
  .photo--folding { left: 600px; top: 0; width: 354px; height: 338px; background: linear-gradient(170deg, #3b2a20 0%, #9c3b2a 30%, #5f93a6 60%, #4a2e22 100%); }
  .photo--bench   { left: 0; top: 312px; width: 312px; height: 244px; z-index: 2; background: linear-gradient(180deg, #c9c7c0 0%, #2dbcc8 45%, #8c8a85 100%); }
  .photo--dresser { left: 294px; top: 248px; width: 306px; height: 308px; z-index: 1; background: linear-gradient(160deg, #a9b4b3 0%, #c7412d 35%, #e5c43a 60%, #2f5ea8 85%, #a9b4b3 100%); }
  .photo--desk    { left: 600px; top: 338px; width: 354px; height: 218px; background: linear-gradient(170deg, #d8cdb2 0%, #b8b5ac 45%, #6b3a26 100%); }
</style>
</head>
<body>
<main class="canvas">
  <section class="card card--front" aria-label="Business card front">
    <header class="brand">
      <h1 class="brand__name">VELVET OAK<br>WORKSHOP</h1>
      <p class="brand__tagline">Your Room - Refreshed</p>
    </header>
    <div class="band band--name">DORA PELL</div>
    <address class="band band--address">
      218 Wexley Blvd. Suite 407 Marlow Bay<br>Florida 32990
    </address>
    <div class="band band--contact">
      321-555-0264<br>www.example-social.test/velvetoakworkshop
    </div>
  </section>

  <section class="card card--back" aria-label="Business card back">
    <div class="photo photo--dining" role="img" aria-label="Photo of a repainted grey dining table with chairs upholstered in yellow"></div>
    <div class="photo photo--stools" role="img" aria-label="Photo of a pub table with blue painted bar stools and patterned seats"></div>
    <div class="photo photo--folding" role="img" aria-label="Photo of a painted teal folding chair beside a Christmas tree"></div>
    <div class="photo photo--bench" role="img" aria-label="Photo of an ornate cast iron garden bench painted turquoise"></div>
    <div class="photo photo--dresser" role="img" aria-label="Photo of a grey dresser with drawers covered in comic book pages"></div>
    <div class="photo photo--desk" role="img" aria-label="Photo of a mid-century desk refinished in cream and wood tones"></div>
  </section>
</main>
</body>
</html>
```